Canvasline Registry, LLC needs clean, modern business card design

Canvasline Registry is based in Honolulu. We offer fine arts collections management and documentation services for private and corporate art collectors. I would like to use my logo (attached). Card can be either single or double sided and either vertical or horizontal. My clients are businesses with art collections (banks, law firms, etc.) and wealthy individual collectors.

```html
<!DOCTYPE html>
<html lang="en">
<head>
<meta charset="utf-8">
<title>Canvasline Registry – Business Card</title>
<link rel="stylesheet" href="https://fonts.googleapis.com/css2?family=Andika:wght@400;700&family=Cabin+Condensed:wght@400;700&display=swap">
<style>
  :root {
    --page-bg: #e9e7e4;
    --card-black: #0b0b0b;
    --card-black-soft: #262626;
    --accent-blue: #1fa3dc;
    --accent-teal: #2a8fa6;
    --text-light: #f1f1f1;
    --text-cream: #e6dccb;
    --text-dark: #141414;
    --logo-ink: #3a3d42;
    --address-ink: #b58a82;
    --panel-light: #e8e2da;
    --panel-mid: #dcd3c9;
  }
  * { margin: 0; padding: 0; box-sizing: border-box; }
  html, body {
    width: 1200px; height: 970px; overflow: hidden;
    background: var(--page-bg);
  }
  .card {
    position: absolute; left: 50px; top: 179px;
    width: 1100px; height: 612px;
    background: var(--card-black);
    box-shadow: 0 10px 30px rgba(0,0,0,0.25);
    overflow: hidden;
    font-family: "Andika", sans-serif;
  }
  .card-head {
    position: absolute; left: 0; top: 0; width: 100%; height: 200px;
    background: radial-gradient(ellipse at 50% 70%, var(--card-black-soft), var(--card-black) 65%);
    text-align: center;
  }
  .holder-name {
    position: absolute; left: 0; right: 0; top: 22px;
    font-family: "Cabin Condensed", sans-serif; font-weight: 700;
    font-size: 66px; line-height: 1;
    background: linear-gradient(90deg, var(--accent-blue), var(--accent-teal));
    -webkit-background-clip: text; background-clip: text; color: transparent;
  }
  .holder-role {
    position: absolute; left: 0; right: 0; top: 95px;
    font-family: "Cabin Condensed", sans-serif;
    font-size: 22px; color: var(--text-light);
  }
  .tagline {
    position: absolute; left: 0; right: 0; top: 152px;
    font-size: 22px; letter-spacing: 0.5px; color: var(--text-cream);
  }
  .rule {
    position: absolute; left: 0; width: 100%; height: 10px;
    background: linear-gradient(90deg, var(--accent-teal), var(--accent-blue) 50%, var(--accent-teal));
  }
  .rule-top { top: 200px; }
  .rule-bottom { top: 485px; }
  .card-body {
    position: absolute; left: 0; top: 210px; width: 100%; height: 275px;
    background: linear-gradient(180deg, var(--panel-light), var(--panel-mid));
  }
  .brand-mark {
    position: absolute; left: 62px; top: 92px;
    display: flex; align-items: center; gap: 18px;
  }
  .brand-name {
    font-family: "Andika", sans-serif; font-weight: 700;
    font-size: 42px; line-height: 1.05; color: var(--logo-ink);
  }
  .brand-dot {
    width: 22px; height: 22px; border-radius: 50%;
    background: var(--accent-teal);
  }
  .divider {
    position: absolute; left: 608px; top: 50px;
    width: 4px; height: 195px; background: var(--text-dark);
  }
  .contact {
    position: absolute; left: 630px; width: 440px; top: 88px;
    text-align: center; color: var(--text-dark);
  }
  .contact-phone { font-size: 32px; letter-spacing: 1.5px; line-height: 1.3; }
  .contact-line { font-size: 25px; letter-spacing: 2px; line-height: 1.65; }
  .card-foot {
    position: absolute; left: 0; top: 495px; width: 100%; height: 117px;
    background: linear-gradient(180deg, var(--card-black-soft), var(--card-black) 60%);
  }
  .address {
    position: absolute; left: 0; right: 0; top: 14px; text-align: center;
    font-family: "Cabin Condensed", sans-serif;
    font-size: 30px; letter-spacing: 1px;
    background: linear-gradient(90deg, var(--address-ink), var(--text-cream) 55%, #d8d0c6);
    -webkit-background-clip: text; background-clip: text; color: transparent;
  }
</style>
</head>
<body>
  <div class="card">
    <header class="card-head">
      <h1 class="holder-name">Leilani M. Hart</h1>
      <p class="holder-role">Owner/Manager</p>
      <p class="tagline">"Fine Arts Collections Management Services"</p>
    </header>
    <div class="rule rule-top"></div>
    <section class="card-body">
      <div class="brand-mark">
        <span class="brand-name">Canvasline<br>Registry</span>
        <span class="brand-dot"></span>
      </div>
      <div class="divider"></div>
      <div class="contact">
        <p class="contact-phone">(808) 555-0147</p>
        <p class="contact-line">www.canvaslineregistry.com</p>
        <p class="contact-line">canvaslineregistry@mail.com</p>
      </div>
    </section>
    <div class="rule rule-bottom"></div>
    <footer class="card-foot">
      <p class="address">1420 Palm Crest Lane Honolulu, HI 96815</p>
    </footer>
  </div>
</body>
</html>
```